Producer Needs a Movie Poster for a Dramatic Film

We need a movie poster for a new dramatic film called "Dust Over Morning".
Synopisis: A young drug addict (cocaine and alcohol), REED MORROW, has hit rock bottom after a continuous downward spiral of alcoholism and drug abuse, leaving him with nothing to live for. His ex-girlfriend left him. His best friend doesn’t want anything to do with him. Unable to rehabilitate himself after multiple attempts, he attempts suicide (Jumping off of a high-rise apartment building).
We want the poster to give the dark feel of the film. It should be serious and personable.
We want the three lead actors to be listed on the top of the poster from left to right (Gerald Pinsk, Corinne Velasq, Darek Ombuvia).
The title of the film, Dust Over Morning, should be in the center of the poster.
We want "Coming Soon" centered on the bottom of the poster.

No pictures will be provided for this poster, so be creative and make something special for us to use. We're looking for a variety of good ideas.

We're excited to see what you come up with!

Please, make sure you provide us with files we can easily use. Also, we would like a copy of the film title in a separate file for easy use as well. So, two files total (One with the poster, One with just the film title by itself).

Industry/Entity Type

Movie

Requirements
Must have
• We want the three lead actors to be listed on the top of the poster from left to right (Gerald Pinsk, Corinne Velasq, Darek Ombuvia).
• The title of the film, Dust Over Morning, should be in the center of the poster.
• We want "Coming Soon" centered on the bottom of the poster.
• Please, make sure you provide us with files we can easily use. Also, we would like a copy of the film title in a separate file for easy use as well. So, two files total (One with the poster, One with just the film title by itself).
Should not have
• Should not have a person on the poster unless they are unrecognizable and you can't see any characteristics. We can't have someone on the poster who won't be in the movie.
• Don't put each locations that won't be in the film either. It takes place in LOs Angeles. Mostly on a high-rise apartment building rooftop.

```html
<!DOCTYPE html>
<html lang="en">
<head>
<meta charset="utf-8">
<title>Dust Over Morning — Poster</title>
<link rel="stylesheet" href="https://fonts.googleapis.com/css2?family=Oswald:wght@700&family=Orbitron:wght@900&family=Bowlby+One&family=Kaushan+Script&display=swap">
<style>
  :root {
    --night: #000000;
    --chalk: #ffffff;
    --window-blue: #1a9ad6;
    --shade: #2a2a2a;
  }
  html, body {
    margin: 0;
    padding: 0;
    width: 849px;
    height: 1200px;
    overflow: hidden;
    background: var(--night);
  }
  .poster {
    position: relative;
    width: 849px;
    height: 1200px;
    background: var(--night);
    overflow: hidden;
  }
  .cast {
    position: absolute;
    top: 62px;
    left: 0;
    width: 849px;
    margin: 0;
    padding: 0;
    list-style: none;
  }
  .cast__name {
    position: absolute;
    width: 200px;
    margin-left: -100px;
    text-align: center;
    font-family: "Oswald", "Arial Narrow", sans-serif;
    font-weight: 700;
    font-size: 31px;
    line-height: 41px;
    color: var(--chalk);
  }
  .cast__name--left { left: 166px; }
  .cast__name--center { left: 422px; }
  .cast__name--right { left: 669px; }
  .artwork {
    position: absolute;
    left: 0;
    top: 0;
  }
  .title-word {
    fill: var(--chalk);
  }
  .title-word--outer {
    font-family: "Orbitron", "Arial Black", sans-serif;
    font-weight: 900;
  }
  .title-word--middle {
    font-family: "Bowlby One", "Arial Black", sans-serif;
    font-style: italic;
  }
  .release {
    position: absolute;
    left: 0;
    top: 1104px;
    width: 849px;
    margin: 0;
    text-align: center;
    font-family: "Kaushan Script", cursive;
    font-size: 46px;
    line-height: 60px;
    color: var(--chalk);
  }
</style>
</head>
<body>
<main class="poster">
  <ul class="cast">
    <li class="cast__name cast__name--left">Gerald<br>Pinsk</li>
    <li class="cast__name cast__name--center">Corinne<br>Velasq</li>
    <li class="cast__name cast__name--right">Darek<br>Ombuvia</li>
  </ul>

  <svg class="artwork" width="849" height="1200" viewBox="0 0 849 1200" xmlns="http://www.w3.org/2000/svg">
    <defs>
      <linearGradient id="tower-side" x1="0" y1="0" x2="0" y2="1">
        <stop offset="0" stop-color="#1a9ad6" stop-opacity="0.85"/>
        <stop offset="1" stop-color="#1a9ad6" stop-opacity="0.6"/>
      </linearGradient>
      <linearGradient id="falling-dust" x1="0" y1="0" x2="0" y2="1">
        <stop offset="0" stop-color="#1a9ad6" stop-opacity="0.55"/>
        <stop offset="1" stop-color="#1a9ad6" stop-opacity="0.08"/>
      </linearGradient>
      <linearGradient id="jumper-tone" x1="0" y1="0" x2="0" y2="1">
        <stop offset="0" stop-color="#3a3a3a"/>
        <stop offset="1" stop-color="#1c1c1c"/>
      </linearGradient>
    </defs>

    <polygon class="tower-side" role="img" aria-label="Blue window pattern on the side of a high-rise tower"
             points="524,240 578,300 578,825 532,851" fill="url(#tower-side)"/>

    <rect class="window-band" role="img" aria-label="Row of lit blue windows" x="289" y="404" width="229" height="54" fill="var(--window-blue)" opacity="0.7"/>
    <rect class="window-band" role="img" aria-label="Row of lit blue windows" x="289" y="644" width="229" height="54" fill="var(--window-blue)" opacity="0.7"/>
    <rect class="falling-windows" role="img" aria-label="Blue windows scattering downward like falling dust" x="289" y="884" width="229" height="224" fill="url(#falling-dust)"/>

    <rect class="jumper" role="img" aria-label="White silhouette of a figure leaping from the rooftop edge"
          x="557" y="210" width="147" height="227" rx="18" fill="url(#jumper-tone)"/>

    <text class="title-word title-word--outer" x="289" y="371" font-size="126" textLength="229" lengthAdjust="spacingAndGlyphs">Dust</text>
    <text class="title-word title-word--middle" x="296" y="590" font-size="118" textLength="215" lengthAdjust="spacingAndGlyphs">Over</text>
    <text class="title-word title-word--outer" x="289" y="851" font-size="126" textLength="229" lengthAdjust="spacingAndGlyphs">Morning</text>
  </svg>

  <p class="release">“Coming Soon”</p>
</main>
</body>
</html>
```